Wine Label for a Prosecco Wine Called Tavi

Prosecco is a white sparkling wine from Italy. We are looking for an eye catching, elegant label for this prosecco that is called "Tavi" because it is a young, fresh, lively white sparkling wine. (We do not want to see children or babies featured on the label-- just the name TAVI please.) Attached is the old label for your reference, and the bottle type that will be used , which is a dark green Burgundy style bottle (pls ignore the label on the bottle). Please no grapes or wine glasses on the label. We are looking for something: eye catching / fun / ELEGANT (not cheap). We would be happy with a fun color too. Remember-- elegant, eye catching! Thanks!
Updates

Hi All, I think I made a mistake in my brief and have updated it. I also uploaded a competitor's label that we like very much to give better direction to what we are looking for. Also, the word Tavi cannot be vertical, nor can it be broken. It needs to read: TAVI or Tavi. Thanks

Target Market(s)

American adults male and female.

Colors
abd036
33a6d7
33b8a4
ffcf3e

Requirements
Must have
• The mandatory information as shown on old labels. The word TAVI should be very prominent.
Nice to have
• The uploaded photo of a competitor's prosecco shows a label we really like... if you could play around with this shape and style we'd be very happy.
Should not have
• No grape images, no wine glass images, no images of babies or children.

```html
<!DOCTYPE html>
<html lang="en">
<head>
<meta charset="utf-8">
<title>Tavi Prosecco – Label</title>
<link rel="stylesheet" href="https://fonts.googleapis.com/css2?family=Oswald:wght@300;400&display=swap">
<style>
  :root {
    --page: #ffffff;
    --navy: #1c2a5e;
    --teal-accent: #1f9cb8;
    --wash-aqua: #5cc4c8;
    --wash-mint: #b4e2da;
  }
  * { margin: 0; padding: 0; box-sizing: border-box; }
  html, body {
    width: 800px; height: 1200px; overflow: hidden;
    background: var(--page);
  }
  .canvas {
    position: relative; width: 800px; height: 1200px;
    display: flex; align-items: center; justify-content: center;
  }
  .label {
    position: relative; width: 718px; height: 668px; overflow: hidden;
    text-align: center; color: var(--navy);
    font-family: "Oswald", sans-serif;
  }
  .label__wash {
    position: absolute; inset: 0;
    background: linear-gradient(170deg, var(--wash-aqua) 0%, var(--wash-mint) 50%, var(--wash-aqua) 100%);
  }
  .label__name {
    position: absolute; left: 0; right: 0; top: 92px;
    font-weight: 400; font-size: 240px; line-height: 1;
    letter-spacing: 14px; text-indent: 14px;
    color: var(--navy);
  }
  .label__style {
    position: absolute; left: 0; right: 0; top: 352px;
    font-weight: 300; font-size: 52px; line-height: 1;
    letter-spacing: 3px; text-indent: 3px;
    color: var(--teal-accent);
  }
  .label__region {
    position: absolute; left: 0; right: 0; top: 492px;
    font-weight: 400; font-size: 30px; line-height: 1;
    transform: scaleX(.9);
  }
  .label__designation {
    position: absolute; left: 0; right: 0; top: 528px;
    font-weight: 300; font-size: 26px; line-height: 1;
    transform: scaleX(.9);
  }
  .label__rule {
    position: absolute; left: 208px; width: 306px; top: 580px;
    height: 1.5px; background: var(--navy);
  }
  .label__type {
    position: absolute; left: 0; right: 0; top: 596px;
    font-weight: 300; font-size: 16px; line-height: 1;
    letter-spacing: 4px; text-indent: 4px;
  }
</style>
</head>
<body>
  <main class="canvas">
    <section class="label">
      <div class="label__wash" role="img" aria-label="Watercolour wash background in aqua and mint tones"></div>
      <h1 class="label__name">TAVI</h1>
      <p class="label__style">Prosecco</p>
      <p class="label__region">VENETO</p>
      <p class="label__designation">Indicazione Geografica Tipica</p>
      <div class="label__rule"></div>
      <p class="label__type">FRIZZANTE</p>
    </section>
  </main>
</body>
</html>
```